Blog Brochure

I am blogging on a weekly basis through Wordpress about business valuation and other financial matters in Dutch.
I would like to digitally use/publish a quarterly booklet/brochure.
My blog is at www.tidrokast.me.
Target Market(s)
SMBs
Industry/Entity Type
Small Business
Font styles to use
Serif
Colors
33b8a4
Requirements
Must have
- Attractive layout, im providing my text in the Mac Pages format
Nice to have
- Keep in touch
- Contact me
- Linkedin and Facebook referring
Should not have
- No English references

```html
<!DOCTYPE html>
<html lang="nl">
<head>
<meta charset="utf-8">
<title>Tidrokast Waarde – Nieuwsbrief</title>
<link href="https://fonts.googleapis.com/css2?family=Lora:wght@400;500;700&display=swap" rel="stylesheet">
<style>
  :root{
    --teal:#33b8a4;
    --teal-dark:#23917f;
    --teal-deep:#1f8a79;
    --teal-light:#5fd0bd;
    --ink:#5f6664;
    --paper:#ffffff;
    --stage:#e9e6e2;
    --photo-a:#e4ebee;
    --photo-b:#b3c3c8;
  }
  *{margin:0;padding:0;box-sizing:border-box}
  html,body{width:1200px;height:1098px;overflow:hidden;background:var(--stage)}
  body{font-family:"Lora",Georgia,serif;position:relative}
  .page{position:absolute;width:318px;height:450px;background:var(--paper);overflow:hidden;box-shadow:0 2px 8px rgba(0,0,0,.25)}
  .p-cover{left:86px;top:70px}
  .p-toc{left:448px;top:70px}
  .p-article{left:811px;top:70px}
  .p-feature{left:86px;top:568px}
  .p-back{left:448px;top:568px;background:var(--teal-deep)}
  .art{position:absolute;left:0;top:0}
  .brand{position:absolute;display:flex;align-items:center;gap:5px;font-weight:700;color:var(--teal-dark);text-transform:uppercase;letter-spacing:.3px;line-height:1;white-space:nowrap}
  .brand-mark{display:block;background:var(--teal-dark)}
  .brand-foot{right:18px;bottom:16px;font-size:9.5px}
  .brand-foot .brand-mark{width:10px;height:10px}
  .brand-cover{left:0;right:0;top:38px;justify-content:center;font-size:17px}
  .brand-cover .brand-mark{width:18px;height:18px}
  .cover-title{position:absolute;left:0;right:0;top:350px;text-align:center;font-weight:400;font-size:20px;color:var(--teal-dark)}
  .cover-sub{position:absolute;left:30px;right:30px;top:380px;text-align:center;font-weight:400;font-size:11px;line-height:15px;color:#555}
  .cover-url{position:absolute;left:0;right:0;top:420px;text-align:center;font-weight:700;font-size:8.5px;color:var(--teal-dark)}
  .heading{position:absolute;left:22px;font-weight:400;font-size:16px;color:var(--teal-dark);white-space:nowrap}
  .heading::after{content:"";display:block;width:34px;height:1.5px;background:var(--teal-dark);margin-top:3px}
  .toc{position:absolute;left:23px;top:118px;width:242px;list-style:none}
  .toc li{display:flex;font-size:6.6px;color:#555;height:18px;align-items:flex-start;white-space:nowrap}
  .toc .dots{flex:1;border-bottom:1px dotted #777;margin:0 1px;height:6px}
  .lead{font-weight:700;color:var(--teal-dark);font-size:8px;line-height:10.2px;text-align:justify}
  .copy{font-size:6.8px;line-height:9px;color:var(--ink);text-align:justify;font-weight:400}
  .copy p+p{margin-top:9px}
  .article-body{position:absolute;left:23px;top:104px;width:273px}
  .article-body .lead{display:inline}
  .col-left{position:absolute;left:20px;top:104px;width:133px}
  .col-left .lead{margin-bottom:12px}
  .feature-photo{position:absolute;left:166px;top:100px;width:131px;height:90px;background:linear-gradient(180deg,var(--photo-a),var(--photo-b))}
  .col-right{position:absolute;left:166px;top:205px;width:131px}
  .back-city{position:absolute;left:0;right:0;top:220px;bottom:0;background:linear-gradient(180deg,rgba(31,138,121,0),rgba(70,185,165,.5) 40%,rgba(50,165,145,.35))}
  .brand-back{left:0;right:0;top:318px;justify-content:center;color:#fff;font-size:16px}
  .brand-back .brand-mark{width:20px;height:20px;background:#fff}
  .contact{position:absolute;left:0;right:0;top:382px;text-align:center;color:#fff;font-size:8.4px;line-height:14px;font-weight:400}
  .social{position:absolute;left:0;right:0;top:428px;display:flex;justify-content:center;gap:4px}
  .social span{width:11px;height:11px;border-radius:50%;background:#fff;display:block}
</style>
</head>
<body>

<section class="page p-cover">
  <svg class="art" width="318" height="450" viewBox="0 0 318 450">
    <defs>
      <linearGradient id="coverPhoto" x1="0" y1="0" x2="0" y2="1">
        <stop offset="0" stop-color="#f1f5f6"/>
        <stop offset="1" stop-color="#b7c6ca"/>
      </linearGradient>
      <linearGradient id="coverCity" x1="0" y1="0" x2="0" y2="1">
        <stop offset="0" stop-color="#ffffff"/>
        <stop offset="1" stop-color="#eef2f2"/>
      </linearGradient>
    </defs>
    <rect width="318" height="450" fill="url(#coverCity)"/>
    <polygon points="0,0 318,0 318,112 160,258 0,190" fill="url(#coverPhoto)" role="img" aria-label="Foto: zakenmensen tillen een stijgende grafiekpijl boven een skyline"/>
    <polygon points="0,190 160,258 318,112 318,190 160,308 0,233" fill="var(--teal)"/>
    <polygon points="0,210 140,300 160,308 0,233" fill="var(--teal-dark)"/>
    <polygon points="160,258 318,112 318,150 175,270" fill="var(--teal-light)"/>
  </svg>
  <div class="brand brand-cover"><span class="brand-mark"></span>Tidrokast Waarde</div>
  <h1 class="cover-title">Nieuwsbrief</h1>
  <p class="cover-sub">Gemijmer, Inspiratie en Informatie over geld, disruptie en KMO bedrijfswaardering</p>
  <p class="cover-url">www.tidrokast.me</p>
</section>

<section class="page p-toc">
  <svg class="art" width="318" height="450" viewBox="0 0 318 450">
    <polygon points="154,0 236,0 214,37" fill="var(--teal-dark)"/>
    <polygon points="214,37 262,0 314,0 250,37" fill="var(--teal)"/>
    <polygon points="232,0 260,0 238,18" fill="#ffffff"/>
  </svg>
  <h2 class="heading" style="top:72px">Inhoudstafel</h2>
  <ol class="toc">
    <li>Waardering van uw kmo, inleiding<span class="dots"></span>1</li>
    <li>Waardering van uw kmo, methodes<span class="dots"></span>2</li>
    <li>Waardering van uw kmo, kasstroom<span class="dots"></span>3</li>
    <li>Waardering van uw kmo, rendement<span class="dots"></span>4</li>
    <li>Waardering van uw kmo, financiering<span class="dots"></span>5</li>
    <li>Waardering van uw kmo, disruptie<span class="dots"></span>6</li>
    <li>Waardering van uw kmo, overname<span class="dots"></span>7</li>
    <li>Waardering van uw kmo, fiscaliteit<span class="dots"></span>8</li>
    <li>Waardering van uw kmo, voorbeeld<span class="dots"></span>9</li>
    <li>Waardering van uw kmo, checklist<span class="dots"></span>10</li>
  </ol>
  <div class="brand brand-foot"><span class="brand-mark"></span>Tidrokast Waarde</div>
</section>

<section class="page p-article">
  <svg class="art" width="318" height="450" viewBox="0 0 318 450">
    <polygon points="154,0 236,0 214,37" fill="var(--teal-dark)"/>
    <polygon points="214,37 262,0 314,0 250,37" fill="var(--teal)"/>
    <polygon points="232,0 260,0 238,18" fill="#ffffff"/>
  </svg>
  <h2 class="heading" style="top:60px">Wat is uw zaak waard?</h2>
  <div class="article-body copy">
    <p><span class="lead">Een onderneming waarderen begint bij een helder beeld van de cijfers, de markt en de plannen voor de komende jaren. Wie dat beeld vroeg opbouwt, onderhandelt later sterker.</span> Elke kmo heeft een eigen verhaal. De omzet, de marge en de klantenbasis vertellen samen hoeveel de zaak vandaag waard is en waar de groei zit. In deze editie bekijken we welke methodes banken en kopers het vaakst gebruiken, hoe u een rendementseis bepaalt en waarom de kasstroom meestal zwaarder weegt dan de winst op papier. We geven ook tips om uw jaarrekening klaar te maken voor een gesprek met een overnemer.</p>
    <p>Daarnaast staan we stil bij disruptie in de financiële wereld. Nieuwe platformen maken kapitaal toegankelijker voor kleine bedrijven, maar vragen ook om meer transparantie. Crowdfunding, digitale kredieten en alternatieve beleggers veranderen de manier waarop ondernemers hun groei financieren. We zetten de voor- en nadelen op een rij en tonen met een concreet voorbeeld hoe een familiebedrijf uit de regio zijn waarde in vijf jaar verdubbelde. Tot slot vindt u een korte checklist die u helpt om elk kwartaal de vinger aan de pols te houden en tijdig bij te sturen.</p>
  </div>
  <div class="brand brand-foot"><span class="brand-mark"></span>Tidrokast Waarde</div>
</section>

<section class="page p-feature">
  <svg class="art" width="318" height="450" viewBox="0 0 318 450">
    <polygon points="154,0 236,0 214,37" fill="var(--teal-dark)"/>
    <polygon points="214,37 262,0 314,0 250,37" fill="var(--teal)"/>
    <polygon points="232,0 260,0 238,18" fill="#ffffff"/>
  </svg>
  <h2 class="heading" style="top:56px">Disruptie en kapitaal</h2>
  <div class="col-left">
    <p class="lead">Een onderneming waarderen begint bij een helder beeld van de cijfers, de markt en de plannen voor de komende jaren en de groei.</p>
    <div class="copy">
      <p>Elke kmo heeft een eigen verhaal. De omzet, de marge en de klantenbasis vertellen samen hoeveel de zaak vandaag waard is en waar de groei zit. In deze editie bekijken we welke methodes banken en kopers het vaakst gebruiken, hoe u een rendementseis bepaalt en waarom de kasstroom meestal zwaarder weegt dan de winst op papier. We geven ook praktische tips om uw jaarrekening klaar te maken voor een gesprek met een investeerder, zodat u goed voorbereid aan tafel zit.</p>
      <p>Wie tijdig plant, houdt de regie in eigen handen en vermijdt verrassingen bij een verkoop.</p>
    </div>
  </div>
  <div class="feature-photo" role="img" aria-label="Foto: zakenmensen tillen een stijgende grafiekpijl boven een skyline"></div>
  <div class="col-right copy">
    <p>Nieuwe platformen maken kapitaal toegankelijker voor kleine bedrijven, maar vragen ook om meer transparantie. Crowdfunding, digitale kredieten en alternatieve beleggers veranderen de manier waarop ondernemers hun groei financieren. We zetten de voor- en nadelen op een rij en tonen met een concreet voorbeeld hoe een familiebedrijf uit de regio zijn waarde in vijf jaar verdubbelde. Tot slot vindt u een korte checklist die u helpt om elk kwartaal de vinger aan de pols te houden en tijdig bij te sturen waar nodig, met aandacht voor marge en werkkapitaal.</p>
  </div>
  <div class="brand brand-foot"><span class="brand-mark"></span>Tidrokast Waarde</div>
</section>

<section class="page p-back">
  <svg class="art" width="318" height="450" viewBox="0 0 318 450">
    <polygon points="0,0 318,0 318,70 159,170 0,70" fill="#1c7f70"/>
    <polygon points="0,70 159,170 318,70 318,120 159,220 0,120" fill="#2c9c8a"/>
    <polygon points="0,120 159,220 318,120 318,150 159,250 0,150" fill="#25917f"/>
  </svg>
  <div class="back-city" role="img" aria-label="Vage skyline van een stad in groenblauwe tinten"></div>
  <div class="brand brand-back"><span class="brand-mark"></span>Tidrokast Waarde</div>
  <div class="contact">
    <p>Neem contact op</p>
    <p>E-mail: hallo@tidrokast.me</p>
    <p>www.tidrokast.me</p>
  </div>
  <div class="social"><span></span><span></span></div>
</section>

</body>
</html>
```